QTR tub packaging design

Hi!
We require a design for two different flavours of packaging for a protein recovery formula.
The design will be for the cardboard tubs as in pic attached. The name of the product will be 'LW recovery formula'. The LW logo is also attached and can be slightly adjusted.
The project will require a design for the front and then a basic design for the information on the back. This will include ingredients, nutrition info, directions and production location. On the back it will also need the 'lift your stride' logo and something referring to 'LW recovery formula by 'Your Vital Ember' (logo for this is attached).
The product will come in two flavours (cacao and coconut, then vanilla and acai) so will need the basic design adjusted for each flavour. The tubs are 1kg and this will need to be somewhere on the front of the tub.
This product is designed for healthy and active people, mainly female focused. The design should be clean and not overloaded with colours and pictures. It should only be two colours max. The final design should communicate that the product will assist people to reach their goals, whilst being health focused.

Target Market(s)

Active Females 20-50

Industry/Entity Type

Nutrition

Requirements
Must have
• Nutrition information and ingredients area
• Three logos attached
• Name- recovery formula
Should not have
• Not too busy, too many pictures or information. Please keep it simple.

```html
<!DOCTYPE html>
<html lang="en">
<head>
<meta charset="utf-8">
<title>LW Recovery Formula by QTR – Tub Fronts</title>
<link rel="stylesheet" href="https://fonts.googleapis.com/css2?family=Josefin+Sans:wght@300;400;600;700&display=swap">
<style>
  :root {
    --backdrop: #f4f3f1;
    --kraft: #c9a57c;
    --kraft-shade: #b8946b;
    --ink: #1f1a16;
    --accent-berry: #c2247a;
    --accent-sky: #2aa3cf;
  }
  * { box-sizing: border-box; margin: 0; padding: 0; }
  html, body {
    width: 1200px;
    height: 909px;
    overflow: hidden;
    background: var(--backdrop);
  }
  .range {
    position: relative;
    width: 1200px;
    height: 909px;
  }
  .tub-front {
    position: absolute;
    top: 30px;
    width: 368px;
    height: 840px;
    background: linear-gradient(90deg, var(--kraft-shade) 0%, var(--kraft) 18%, var(--kraft) 82%, var(--kraft-shade) 100%);
    border-radius: 10px;
    color: var(--ink);
    font-family: "Josefin Sans", "Helvetica Neue", Arial, sans-serif;
    text-align: center;
  }
  .tub-front--cacao { left: 150px; --accent: var(--accent-berry); }
  .tub-front--vanilla { left: 712px; --accent: var(--accent-sky); }

  .product-mark {
    position: absolute;
    top: 330px;
    left: 0;
    right: 0;
    font-size: 112px;
    font-weight: 700;
    line-height: 1;
    letter-spacing: -2px;
    color: var(--accent);
  }
  .product-name {
    position: absolute;
    top: 440px;
    left: 0;
    right: 0;
    line-height: 1.15;
  }
  .product-name__line1 {
    display: block;
    font-size: 27px;
    font-weight: 300;
    letter-spacing: 0.5px;
  }
  .product-name__line2 {
    display: block;
    font-size: 25px;
    font-weight: 400;
    letter-spacing: 4px;
  }
  .product-name__by {
    display: block;
    font-size: 24px;
    font-weight: 400;
    margin-top: 4px;
  }
  .maker-mark {
    position: absolute;
    top: 608px;
    left: 0;
    right: 0;
    display: flex;
    justify-content: center;
    align-items: center;
    gap: 8px;
    font-size: 48px;
    font-weight: 700;
    line-height: 1;
  }
  .maker-mark__dot {
    width: 12px;
    height: 12px;
    border-radius: 50%;
    background: var(--ink);
    margin-top: -30px;
  }
  .flavour-panel {
    position: absolute;
    top: 692px;
    left: 33px;
    width: 300px;
    height: 46px;
  }
  .flavour-panel svg { position: absolute; inset: 0; }
  .flavour-panel__flavour {
    position: absolute;
    top: 6px;
    left: 0;
    width: 244px;
    font-size: 17px;
    font-weight: 300;
    letter-spacing: 1px;
  }
  .flavour-panel__type {
    position: absolute;
    top: 29px;
    left: 0;
    width: 244px;
    font-size: 11px;
    font-weight: 300;
    letter-spacing: 3px;
  }
  .flavour-panel__weight {
    position: absolute;
    top: 10px;
    left: 250px;
    width: 50px;
    font-size: 18px;
    font-weight: 700;
  }
</style>
</head>
<body>
<main class="range">
  <article class="tub-front tub-front--cacao">
    <div class="product-mark">LW</div>
    <p class="product-name">
      <span class="product-name__line1">RECOVERY</span>
      <span class="product-name__line2">FORMULA</span>
      <span class="product-name__by">by</span>
    </p>
    <div class="maker-mark"><span>QTR</span><span class="maker-mark__dot"></span></div>
    <div class="flavour-panel">
      <svg width="300" height="46" viewBox="0 0 300 46" aria-hidden="true">
        <rect x="0.5" y="0.5" width="244" height="45" fill="none" stroke="#1f1a16" stroke-width="1"/>
        <line x1="0" y1="26" x2="244" y2="26" stroke="#1f1a16" stroke-width="1"/>
      </svg>
      <span class="flavour-panel__flavour">CACAO AND COCONUT</span>
      <span class="flavour-panel__type">DIETARY SUPPLEMENT</span>
      <span class="flavour-panel__weight">1Kg</span>
    </div>
  </article>

  <article class="tub-front tub-front--vanilla">
    <div class="product-mark">LW</div>
    <p class="product-name">
      <span class="product-name__line1">RECOVERY</span>
      <span class="product-name__line2">FORMULA</span>
      <span class="product-name__by">by</span>
    </p>
    <div class="maker-mark"><span>QTR</span><span class="maker-mark__dot"></span></div>
    <div class="flavour-panel">
      <svg width="300" height="46" viewBox="0 0 300 46" aria-hidden="true">
        <rect x="0.5" y="0.5" width="244" height="45" fill="none" stroke="#1f1a16" stroke-width="1"/>
        <line x1="0" y1="26" x2="244" y2="26" stroke="#1f1a16" stroke-width="1"/>
      </svg>
      <span class="flavour-panel__flavour">CACAO AND COCONUT</span>
      <span class="flavour-panel__type">DIETARY SUPPLEMENT</span>
      <span class="flavour-panel__weight">1Kg</span>
    </div>
  </article>
</main>
</body>
</html>
```